Startup Drone Platform Company business card

We are needing a business card design for our employees. We are a startup drone platform. We are looking for a business card that has our logo on one side, with the employee/company details on the opposite side. We are looking for something that is very eye catching, modern, and bold.

Target Market(s)

This will target both drone pilots and drone businesses, along with all the industries that could utilize drone services (aerial video, aerial photos, inspections, 3d mapping, etc).

Industry/Entity Type

Business

```html
<!DOCTYPE html>
<html lang="en">
<head>
<meta charset="utf-8">
<title>Skyward Hire – Business Card</title>
<link href="https://fonts.googleapis.com/css2?family=Lato:wght@400;700&display=swap" rel="stylesheet">
<style>
  :root {
    --stage: #e4e4e2;
    --card-dark: #4a4a4a;
    --card-light: #ffffff;
    --teal: #3bb8c3;
    --ink: #2d2d2d;
    --muted: #555555;
    --grey-band: #4a4a4a;
  }
  * { margin: 0; padding: 0; box-sizing: border-box; }
  html, body {
    width: 1200px; height: 810px; overflow: hidden;
    background: var(--stage);
    font-family: "Lato", Arial, sans-serif;
  }
  .canvas { position: relative; width: 1200px; height: 810px; }

  .card {
    position: absolute;
    width: 600px; height: 343px;
    box-shadow: 0 6px 18px rgba(0,0,0,0.18);
    overflow: hidden;
  }

  /* Back of card */
  .card--back { left: 70px; top: 40px; background: var(--card-dark); color: #fff; }
  .card--back .brand {
    position: absolute; left: 0; right: 0; top: 130px;
    display: flex; align-items: center; justify-content: center; gap: 14px;
  }
  .brand-dot {
    width: 14px; height: 14px; border-radius: 50%;
    background: var(--teal);
  }
  .brand-name {
    font-weight: 400; font-size: 28px; letter-spacing: 9px;
    text-transform: uppercase;
  }
  .card--back .brand-name { color: #ffffff; }
  .card--back .web {
    position: absolute; left: 0; right: 0; top: 270px;
    text-align: center; font-size: 15px; letter-spacing: 0.5px;
  }

  /* Front of card */
  .card--front { left: 530px; top: 427px; background: var(--card-light); }
  .card--front .brand {
    position: absolute; left: 40px; top: 140px;
    display: flex; align-items: center; gap: 12px;
  }
  .card--front .brand-name { color: var(--ink); font-size: 22px; letter-spacing: 6px; }
  .divider { position: absolute; left: 0; top: 0; width: 600px; height: 343px; }
  .swoosh { position: absolute; left: 0; top: 0; width: 600px; height: 343px; }

  .details { position: absolute; left: 340px; top: 34px; color: var(--ink); }
  .person-name { color: var(--teal); font-size: 24px; font-weight: 400; }
  .person-role { font-size: 13px; color: var(--muted); margin-top: 2px; }
  .address { font-size: 14px; line-height: 20px; margin-top: 14px; color: var(--muted); }
  .contact { list-style: none; margin-top: 6px; font-size: 14px; line-height: 22px; color: var(--muted); }
  .contact li { display: flex; align-items: center; gap: 8px; }
  .contact svg { width: 13px; height: 13px; fill: var(--teal); flex: none; }
</style>
</head>
<body>
<main class="canvas">

  <section class="card card--back" aria-label="Card back">
    <div class="brand">
      <span class="brand-dot"></span>
      <span class="brand-name">Skyward Hire</span>
    </div>
    <p class="web">www.skywardhire.com</p>
  </section>

  <section class="card card--front" aria-label="Card front">
    <svg class="swoosh" viewBox="0 0 600 343" aria-hidden="true">
      <path d="M0 343 L600 343 L600 235 C470 300 250 335 0 343 Z" fill="var(--grey-band)"/>
      <path d="M0 343 C250 332 460 290 600 222 L600 236 C460 298 250 336 0 343 Z" fill="var(--teal)"/>
    </svg>
    <svg class="divider" viewBox="0 0 600 343" aria-hidden="true">
      <line x1="300" y1="80" x2="345" y2="250" stroke="var(--teal)" stroke-width="1.2"/>
    </svg>

    <div class="brand">
      <span class="brand-dot"></span>
      <span class="brand-name">Skyward Hire</span>
    </div>

    <div class="details">
      <h1 class="person-name">Dana Whitfield</h1>
      <p class="person-role">President &amp; CEO</p>
      <p class="address">417 NW Birchwood Ave<br>Suite 212<br>Oak Ridge, MO 64190</p>
      <ul class="contact">
        <li>
          <svg viewBox="0 0 24 24"><path d="M6.6 10.8a15.1 15.1 0 0 0 6.6 6.6l2.2-2.2a1 1 0 0 1 1-.25 11.4 11.4 0 0 0 3.6.57 1 1 0 0 1 1 1V20a1 1 0 0 1-1 1A17 17 0 0 1 3 4a1 1 0 0 1 1-1h3.5a1 1 0 0 1 1 1c0 1.25.2 2.45.57 3.57a1 1 0 0 1-.25 1z"/></svg>
          877.555.0146
        </li>
        <li>
          <svg viewBox="0 0 24 24"><path d="M2 5h20v14H2z M2 5l10 8 10-8" fill="none" stroke="var(--teal)" stroke-width="2"/></svg>
          info@skywardhire.com
        </li>
        <li>
          <svg viewBox="0 0 24 24"><circle cx="12" cy="12" r="10"/><path d="M2 12h20M12 2c3 3 3 17 0 20M12 2c-3 3-3 17 0 20" stroke="#fff" stroke-width="1.4" fill="none"/></svg>
          www.skywardhire.com
        </li>
      </ul>
    </div>
  </section>

</main>
</body>
</html>
```